New Business Card Design Project

Hi there

Could you please make a design that is soft and appealing to people who would purchase gemstones, buy healing jewellery, seek counselling, may seek energy healing and/or learn English. Essentially I'm looking for something with a soft human design. Please incorporate the logo and select font that can be easily read and softer images in the background - but not too busy. I would like it double sided as well.

Optional: Elements could include gemstones, feathers, plants and images that are happy and calming.

Target Market(s)

People into alternative health, those from non-English speaking backgrounds, businesses

Contact Information for Business Card

Lena Whitford
Mobile: 0418 265 093, Facebook and Instagram Logos,
ABN: 61 472 185 034 (Australian Business Number - small at the bottom)

Requirements
Must have
• My project must have:
- Meadow Thread logo
- Symbols that represent the 4 main services: 1. Gemstones/jewellery, 2. counselling, 3. meditation/energy healing, 4. education
Nice to have
• Clear and easy to read.

```html
<!DOCTYPE html>
<html lang="en">
<head>
<meta charset="utf-8">
<title>Meadow Thread – Business Card</title>
<link href="https://fonts.googleapis.com/css2?family=Montserrat:wght@400;500;700&display=swap" rel="stylesheet">
<style>
  :root {
    --backdrop: #d3d3d3;
    --card-white: #ffffff;
    --teal: #1ab3a8;
    --teal-deep: #119c93;
    --teal-light: #7fd3c8;
    --leaf-green: #7cb82f;
    --text-teal: #1aa89d;
    --photo-cream: #efe6cf;
    --photo-leaf: #6aa86a;
    --photo-stone: #dcd8e6;
  }
  * { box-sizing: border-box; margin: 0; padding: 0; }
  html, body { width: 1200px; height: 800px; overflow: hidden; }
  body {
    background: var(--backdrop);
    font-family: "Montserrat", sans-serif;
    position: relative;
  }
  .card {
    position: absolute;
    top: 240px;
    width: 540px;
    height: 309px;
    overflow: hidden;
    box-shadow: 0 6px 18px rgba(0,0,0,0.18);
  }
  .card--front { left: 40px; background: var(--teal); }
  .card--back { left: 620px; background: var(--card-white); }

  /* Front */
  .front-photo {
    position: absolute; inset: 0;
    background:
      linear-gradient(90deg, var(--teal-deep) 0%, var(--teal) 30%, rgba(26,179,168,0.55) 52%, rgba(26,179,168,0) 75%),
      radial-gradient(ellipse at 78% 35%, var(--photo-leaf) 0%, rgba(106,168,106,0) 45%),
      radial-gradient(ellipse at 85% 75%, var(--photo-stone) 0%, rgba(220,216,230,0) 55%),
      linear-gradient(180deg, var(--photo-cream), #e8efe6);
  }
  .front-brand {
    position: absolute; left: 52px; top: 118px;
    display: flex; align-items: center; gap: 16px;
  }
  .brand-dot {
    width: 46px; height: 46px; border-radius: 50%;
    border: 2px solid #fff;
  }
  .brand-name {
    color: #fff; font-size: 30px; font-weight: 400;
    letter-spacing: 3px; text-transform: uppercase; line-height: 1.05;
  }
  .front-rule {
    position: absolute; left: 52px; top: 200px;
    width: 300px; height: 1.5px; background: #fff;
  }

  /* Back */
  .back-brand {
    position: absolute; right: 40px; top: 34px;
    display: flex; align-items: center; gap: 12px;
  }
  .back-brand .brand-dot { width: 34px; height: 34px; border-color: var(--teal); }
  .back-brand .brand-name { color: var(--teal); font-size: 22px; letter-spacing: 2px; }
  .social {
    position: absolute; right: 40px; top: 92px;
    display: flex; gap: 5px;
  }
  .social span { width: 14px; height: 14px; border-radius: 3px; background: var(--leaf-green); }
  .back-rule {
    position: absolute; left: 40px; right: 40px; top: 118px;
    height: 1.5px; background: var(--teal);
  }
  .services {
    position: absolute; right: 40px; top: 132px;
    display: flex; gap: 10px;
  }
  .service {
    width: 46px; height: 46px; border-radius: 4px;
  }
  .service--gems { background: linear-gradient(135deg, #555, #c9c9d6); }
  .service--counsel { background: #cdeef2; }
  .service--meditate { background: #f2eef6; }
  .service--learn { background: #f3f3f3; border-radius: 50%; border: 2px solid #222; }

  .contact {
    position: absolute; left: 40px; top: 178px; color: var(--text-teal);
  }
  .contact-name {
    color: var(--leaf-green); font-weight: 700; font-size: 19px;
    letter-spacing: 0.5px; text-transform: uppercase;
  }
  .contact-abn { font-size: 12px; margin-top: 3px; }
  .contact-rule { width: 200px; height: 1.5px; background: var(--teal); margin: 8px 0 8px; }
  .contact-line { display: flex; align-items: center; gap: 8px; font-size: 12.5px; line-height: 19px; }
  .contact-line svg { width: 12px; height: 12px; flex: none; }
</style>
</head>
<body>
  <section class="card card--front">
    <div class="front-photo" role="img" aria-label="Soft photo of gemstones, crystals, feathers, sage and green leaves fading into teal"></div>
    <div class="front-brand">
      <span class="brand-dot"></span>
      <span class="brand-name">Meadow<br>Thread</span>
    </div>
    <div class="front-rule"></div>
  </section>

  <section class="card card--back">
    <div class="back-brand">
      <span class="brand-dot"></span>
      <span class="brand-name">Meadow Thread</span>
    </div>
    <div class="social" aria-label="Social media"><span></span><span></span></div>
    <div class="back-rule"></div>
    <div class="services">
      <div class="service service--gems" role="img" aria-label="Gemstones and jewellery"></div>
      <div class="service service--counsel" role="img" aria-label="Counselling"></div>
      <div class="service service--meditate" role="img" aria-label="Meditation and energy healing"></div>
      <div class="service service--learn" role="img" aria-label="Education"></div>
    </div>
    <div class="contact">
      <div class="contact-name">Lena Whitford</div>
      <div class="contact-abn">ABN: 61 472 185 034</div>
      <div class="contact-rule"></div>
      <div class="contact-line">
        <svg viewBox="0 0 12 12"><path d="M2 1l2 0 1 3-1.5 1a6 6 0 0 0 3.5 3.5l1-1.5 3 1v2a1 1 0 0 1-1 1A10 10 0 0 1 1 2a1 1 0 0 1 1-1z" fill="#7cb82f"/></svg>
        0418 265 093
      </div>
      <div class="contact-line">
        <svg viewBox="0 0 12 12"><rect x="0.7" y="2.2" width="10.6" height="7.6" fill="none" stroke="#7cb82f" stroke-width="1.2"/><path d="M1 2.5l5 4 5-4" fill="none" stroke="#7cb82f" stroke-width="1.2"/></svg>
        hello@meadowthread.com
      </div>
      <div class="contact-line">
        <svg viewBox="0 0 12 12"><circle cx="6" cy="6" r="5.2" fill="none" stroke="#7cb82f" stroke-width="1.2"/><path d="M0.8 6h10.4M6 0.8c-2.5 3-2.5 7.4 0 10.4M6 0.8c2.5 3 2.5 7.4 0 10.4" fill="none" stroke="#7cb82f" stroke-width="1"/></svg>
        www.meadowthread.com
      </div>
    </div>
  </section>
</body>
</html>
```